Bright Harbour Tutors Facebook business page

I currently have a website with a CSS template www.brightharbourtutors.co.uk. I am now seeking to have graphics designed in a complimentary style for:

1. A Facebook business landing page
Updates

Dear all,

Thank you to those of you that have submitted designs so far.  Please note that the brief and title of this project has changed.  I now simply require a Facebook business page designing and not a Twitter and Youtube page also.

I hope that you will all find the budget more attractive now.

Regards

Gareth

Dear all,  your submissions sor far have been very creative.  As further guidance, I would like to see an innovative and creative adaptation and/or embellishment of my 'digital man'.  He could in some way be indicating a call to action to 'like' my page.

The use also of an additional key message: The future of marketing is digital 

This could be integral to a design theme.

I hope that this helps.

Thank you all

Gareth

Target Market(s)

Small and medium sized businesses, students 18-25, Apprentices, marketing professionals

Industry/Entity Type

Business

Requirements
Must have
• Ideally, my logo must appear each page with my slogan 'let us teach you how'. The font used is Arial Rounded MT. For the Facebook landing page, I would like the call to action to be 'getting people to like my page'. Therefore a innovative way of pointing to the like button (see http://www.plumvex.example/zestorafizz). Maybe this could be an adaptation of my icon, the digital man. It needs to be innovative and eyecatching whilst maintaing my corporate colours. I teach courses in Social Media so I need to have impressive pages! I also am keen to see what creative ideas you can come up with!

```html
<!DOCTYPE html>
<html lang="en">
<head>
<meta charset="utf-8">
<title>Bright Harbour Tutors – Facebook landing page</title>
<link rel="stylesheet" href="https://fonts.googleapis.com/css2?family=Varela+Round&display=swap">
<style>
  :root {
    --brand-yellow: #f7b51b;
    --ink-dark: #3a3a3a;
    --ink-mid: #5c5c5c;
    --panel-top: #e4e4e4;
    --panel-light: #f6f6f6;
    --header-band: #d9d9d9;
    --card-fill: #fafafa;
    --page-bg: #ffffff;
  }
  * { box-sizing: border-box; margin: 0; padding: 0; }
  html, body {
    width: 874px; height: 1200px; overflow: hidden;
    background: var(--page-bg);
    font-family: "Varela Round", Arial, sans-serif;
  }
  .landing {
    position: relative;
    width: 874px; height: 1200px;
  }
  .panel {
    position: absolute; left: 10px; top: 0;
    width: 826px; height: 1192px;
    background: radial-gradient(ellipse at 50% 35%, var(--panel-light) 0%, #efefef 45%, var(--panel-top) 100%);
  }
  .contact-band {
    position: absolute; left: 0; top: 0;
    width: 826px; height: 116px;
    background: linear-gradient(to bottom, var(--header-band), #e6e6e6);
  }
  .contact {
    position: absolute; left: 26px; top: 38px;
    font-size: 34px; color: var(--ink-mid);
  }
  .contact .phone {
    color: var(--brand-yellow);
    font-size: 42px;
    margin-left: 8px;
  }
  .like-badge {
    position: absolute; left: 640px; top: 14px;
    width: 232px; height: 232px;
  }
  .brand-mark {
    position: absolute; left: 320px; top: 170px;
    width: 190px; height: 190px;
    border-radius: 50%;
    background: var(--brand-yellow);
  }
  .brand-name {
    position: absolute; left: 0; top: 412px;
    width: 826px; text-align: center;
    font-size: 52px; color: var(--ink-dark);
  }
  .slogan {
    position: absolute; left: 38px; top: 496px;
    font-size: 58px; color: var(--ink-mid);
  }
  .service {
    position: absolute; left: 33px;
    width: 684px; height: 168px;
    background: var(--card-fill);
    border-radius: 28px;
    padding: 24px 0 0 72px;
  }
  .service h2 {
    font-weight: 400;
    font-size: 44px; color: var(--ink-dark);
    line-height: 1;
    margin-bottom: 14px;
  }
  .service p {
    font-size: 23px; color: var(--ink-dark);
    line-height: 1.25;
  }
  .service--social { top: 616px; }
  .service--mobile { top: 796px; }
  .service--analytics { top: 976px; }
</style>
</head>
<body>
<main class="landing">
  <section class="panel">
    <header class="contact-band">
      <p class="contact">Get in touch <span class="phone">0845 730 284</span></p>
    </header>

    <div class="brand-mark" aria-hidden="true"></div>
    <h1 class="brand-name">Bright Harbour Tutors</h1>
    <p class="slogan">Let us teach you how</p>

    <article class="service service--social">
      <h2>SOCIAL MEDIA</h2>
      <p>Create the conversation<br>Build a relationship</p>
    </article>
    <article class="service service--mobile">
      <h2>MOBILE MARKETING</h2>
      <p>Engage with your customers<br>Reach a larger audience</p>
    </article>
    <article class="service service--analytics">
      <h2>WEB ANALYTICS</h2>
      <p>Measure your marketing<br>Maximise your return on investment</p>
    </article>
  </section>

  <svg class="like-badge" viewBox="0 0 232 232" role="img" aria-label="Like our page call to action">
    <circle cx="116" cy="116" r="112" fill="#ffffff"/>
    <circle cx="116" cy="116" r="104" fill="var(--brand-yellow)"/>
    <text x="116" y="108" text-anchor="middle" font-family="Varela Round, Arial, sans-serif" font-size="30" fill="var(--ink-dark)">LIKE OUR</text>
    <text x="116" y="146" text-anchor="middle" font-family="Varela Round, Arial, sans-serif" font-size="30" fill="var(--ink-dark)">PAGE</text>
  </svg>
</main>
</body>
</html>
```